Kelmora Business Card

We want a logo that connects with the target consumer who are Retailers in the giftware/wholesale/ecommerce space. We will be constantly changing product lines and industry. We are after a logo that can communicate the meaning of "Kelmora"which means Divine/spiritual/light. The company name and owners are of Indian nationals and want to bring the positivity/growth in the design as a subtle message.
Have attached a logo that we think captures the essence of the word "Kelmora" which is light/glow/divine.

Target Market(s)

Adults based in Australia english speaking aged 20 - 60 years that are in the retail business.

Industry/Entity Type

Business

Font styles to use
Serif
Sans Serif
Decorative
Script

Requirements
Must have
• Logo in form of "D" or "Kelmora" or "Kelmora Pty Ltd"
Nice to have
• I have attached a sample of letter D used as logo. Its shows the glowing sun which is representative/symbolic presentation of word "Kelmora"

```html
<!DOCTYPE html>
<html lang="en">
<head>
<meta charset="utf-8">
<title>Kelmora Business Card</title>
<link href="https://fonts.googleapis.com/css2?family=Ubuntu:wght@400;500;700&display=swap" rel="stylesheet">
<style>
  :root {
    --backdrop: #8f8f8f;
    --card: #f7f7f5;
    --ink: #ffffff;
    --brand: #1d6fb8;
    --sun: #f2a527;
    --green: #1f9a4a;
    --blue: #1a9ad6;
    --red: #a3001e;
    --indigo: #545c9c;
    --mauve: #b07a8c;
    --gold: #ddab06;
  }
  html, body {
    margin: 0;
    width: 1200px;
    height: 1000px;
    overflow: hidden;
    background: var(--backdrop);
    font-family: "Ubuntu", sans-serif;
  }
  .canvas {
    position: relative;
    width: 1200px;
    height: 1000px;
  }
  .card {
    position: absolute;
    left: 250px;
    width: 700px;
    height: 400px;
    background: var(--card);
    box-shadow: 0 6px 18px rgba(0,0,0,0.25);
    overflow: hidden;
  }
  .card-front { top: 70px; }
  .card-back { top: 530px; }

  .brand {
    display: flex;
    align-items: center;
    justify-content: center;
    gap: 14px;
    color: var(--brand);
    font-weight: 700;
  }
  .brand-dot {
    border-radius: 50%;
    background: var(--sun);
  }
  .card-front .brand {
    height: 100%;
    font-size: 92px;
  }
  .card-front .brand-dot { width: 56px; height: 56px; }

  .card-back .brand {
    position: absolute;
    top: 34px;
    left: 0;
    right: 0;
    font-size: 40px;
    gap: 8px;
  }
  .card-back .brand-dot { width: 24px; height: 24px; }

  .band {
    position: absolute;
    display: flex;
    align-items: center;
    color: var(--ink);
    box-sizing: border-box;
  }
  .band-name    { left: 0; top: 118px; width: 350px; height: 50px; background: var(--green); padding-left: 56px; font-size: 23px; }
  .band-title   { left: 0; top: 180px; width: 330px; height: 46px; background: var(--blue);  padding-left: 44px; font-size: 18px; }
  .band-address { left: 0; top: 238px; width: 300px; height: 62px; background: var(--red);   padding-left: 28px; font-size: 15px; line-height: 1.3; }
  .band-phone   { left: 390px; top: 196px; width: 290px; height: 50px; background: var(--indigo); padding-left: 26px; font-size: 18px; }
  .band-email   { left: 370px; top: 258px; width: 310px; height: 50px; background: var(--mauve);  padding-left: 26px; font-size: 18px; }
  .band-web     { left: 350px; top: 320px; width: 330px; height: 54px; background: var(--gold);   padding-left: 26px; font-size: 18px; }
</style>
</head>
<body>
<main class="canvas">
  <section class="card card-front" aria-label="Card front">
    <div class="brand">
      <span class="brand-dot"></span>
      <span class="brand-name">Kelmora</span>
    </div>
  </section>

  <section class="card card-back" aria-label="Card back">
    <div class="brand">
      <span class="brand-dot"></span>
      <span class="brand-name">Kelmora</span>
    </div>
    <div class="band band-name">Your Name</div>
    <div class="band band-title">Job Title</div>
    <div class="band band-address">A : 45 Orchard Lane, Fenwick Bay<br>Harbourside, Australia</div>
    <div class="band band-phone">P : 012- 345- 6789</div>
    <div class="band band-email">M : yourmail@mail,com</div>
    <div class="band band-web">W : www.address.com</div>
  </section>
</main>
</body>
</html>
```